Business card design needed

Chasing a very simplistic modern design with a logo incorporating "TRV".
I'm starting a plumbing business.
I do water, sanitary and drainage plumbing that will cover residential, commercial, rental, rural, excavation, new housing and all maintanence requirements.

Industry/Entity Type

Business

Contact Information for Business Card

TRV PLUMBING SERVICES
DEAN HOLLOWBY - LICENSED PLUMBER
PHONE: 0481926574
E-MAIL: hollodt7@wirelane.com
NORTHERN SUBURBS

Requirements
Must have
• lower case email address

```html
<!DOCTYPE html>
<html lang="en">
<head>
<meta charset="utf-8">
<title>TRV Plumbing Services – Business Card</title>
<link rel="stylesheet" href="https://fonts.googleapis.com/css2?family=Dosis:wght@500;600;700&display=swap">
<style>
  :root {
    --brand-blue: #1f46ea;
    --brand-blue-deep: #1634c4;
    --card-white: #ffffff;
    --backdrop: #e9eaee;
    --card-shadow: rgba(20, 24, 40, 0.18);
  }
  * { box-sizing: border-box; margin: 0; padding: 0; }
  html, body {
    width: 1200px;
    height: 741px;
    overflow: hidden;
  }
  body {
    background: var(--backdrop);
    font-family: "Dosis", sans-serif;
    position: relative;
  }
  .card {
    position: absolute;
    width: 540px;
    height: 309px;
    background: var(--card-white);
    box-shadow: 0 6px 18px var(--card-shadow);
    overflow: hidden;
  }
  .card--front { left: 40px; top: 216px; }
  .card--back  { left: 620px; top: 216px; }

  .card__wave {
    position: absolute;
    inset: 0;
    width: 100%;
    height: 100%;
  }

  .holder-name {
    position: absolute;
    left: 32px;
    top: 26px;
    color: var(--brand-blue);
    font-weight: 700;
    font-size: 46px;
    letter-spacing: 2px;
    line-height: 1;
  }

  .brand {
    position: absolute;
    display: flex;
    flex-direction: column;
    align-items: flex-end;
  }
  .card--front .brand { right: 30px; top: 80px; }
  .card--back .brand  { right: 30px; top: 26px; }

  .brand__mark {
    display: flex;
    align-items: center;
    gap: 8px;
    color: var(--brand-blue);
    font-weight: 700;
    font-size: 78px;
    line-height: 0.9;
    letter-spacing: 1px;
  }
  .brand__dot {
    width: 14px;
    height: 14px;
    border-radius: 50%;
    background: var(--brand-blue);
  }
  .brand__tagline {
    color: var(--card-white);
    font-weight: 600;
    font-size: 20px;
    letter-spacing: 1px;
    line-height: 1;
  }
  .card--front .brand__tagline { margin-top: 48px; }
  .card--back .brand__tagline  { margin-top: 52px; }

  .contact {
    position: absolute;
    left: 30px;
    bottom: 24px;
    list-style: none;
    color: var(--card-white);
    font-weight: 600;
    font-size: 18px;
    letter-spacing: 1px;
    line-height: 1.6;
  }
  .contact__email { text-transform: none; }

  .services {
    position: absolute;
    left: 40px;
    bottom: 20px;
    list-style: none;
    color: var(--card-white);
    font-weight: 600;
    font-size: 26px;
    letter-spacing: 1.5px;
    line-height: 1.5;
  }
  .services__item {
    display: flex;
    align-items: center;
    gap: 16px;
  }
  .services__bullet {
    width: 13px;
    height: 13px;
    border-radius: 50%;
    background: var(--card-white);
    flex: none;
  }
</style>
</head>
<body>

  <section class="card card--front" aria-label="Business card front">
    <svg class="card__wave" viewBox="0 0 540 309" preserveAspectRatio="none" aria-hidden="true">
      <defs>
        <linearGradient id="front-wave-fill" x1="0" y1="0" x2="0" y2="1">
          <stop offset="0" stop-color="#1f46ea"/>
          <stop offset="1" stop-color="#1634c4"/>
        </linearGradient>
      </defs>
      <path d="M0,146 C120,118 250,120 360,158 C430,180 490,186 540,182 L540,309 L0,309 Z" fill="url(#front-wave-fill)"/>
    </svg>

    <h1 class="holder-name">DEAN HOLLOWBY</h1>

    <div class="brand">
      <div class="brand__mark"><span>TRV</span><span class="brand__dot"></span></div>
      <div class="brand__tagline">PLUMBING SERVICES</div>
    </div>

    <ul class="contact">
      <li>CALL: 0481926574</li>
      <li>MAILTO: <span class="contact__email">hollodt7@wirelane.com</span></li>
      <li>NORTHERN SUBURBS</li>
    </ul>
  </section>

  <section class="card card--back" aria-label="Business card back">
    <svg class="card__wave" viewBox="0 0 540 309" preserveAspectRatio="none" aria-hidden="true">
      <defs>
        <linearGradient id="back-wave-fill" x1="0" y1="0" x2="0" y2="1">
          <stop offset="0" stop-color="#1f46ea"/>
          <stop offset="1" stop-color="#1634c4"/>
        </linearGradient>
      </defs>
      <path d="M0,152 C120,136 240,146 330,138 C420,130 490,112 540,96 L540,309 L0,309 Z" fill="url(#back-wave-fill)"/>
    </svg>

    <div class="brand">
      <div class="brand__mark"><span>TRV</span><span class="brand__dot"></span></div>
      <div class="brand__tagline">PLUMBING SERVICES</div>
    </div>

    <ul class="services">
      <li class="services__item"><span class="services__bullet"></span>WATER</li>
      <li class="services__item"><span class="services__bullet"></span>SANITARY</li>
      <li class="services__item"><span class="services__bullet"></span>DRAINAGE PLUMBING</li>
    </ul>
  </section>

</body>
</html>
```